Salon website

Need a web design for a new blow dry and hair extension boutique in CT
would like the color scheme to be gray, white and tiffany blue
Create a web site with about 4 pages showing
1 about us page
1 blow dry services page
1 hair extension services page
1 contact us page
1 membership page
1 parties page

Industry/Entity Type

Boutique

Colors
86cfc6
cfeae6
33b7a4
aaaaaa
cbcbcb
ffffff

```html
<!DOCTYPE html>
<html lang="en">
<head>
<meta charset="utf-8">
<title>Blow Dry and Hair Extension Boutique – Contact Us</title>
<link href="https://fonts.googleapis.com/css2?family=PT+Sans:ital,wght@0,400;0,700;1,400&display=swap" rel="stylesheet">
<style>
  :root {
    --tiffany: #1fb6ae;
    --tiffany-deep: #0e7f7a;
    --tiffany-light: #4ecac4;
    --field: rgba(38, 170, 160, 0.88);
    --panel: rgba(112, 112, 112, 0.72);
    --hero-bg: #e8e8e8;
    --photo-dark: #4a3a31;
    --photo-warm: #9c7057;
    --footer-bg: #e6e6e6;
    --white: #ffffff;
    --ink-muted: #7a7a7a;
    --nav-active: #555555;
  }
  * { box-sizing: border-box; margin: 0; padding: 0; }
  html, body { width: 1200px; height: 989px; overflow: hidden; background: var(--white); }
  body { position: relative; font-family: "PT Sans", sans-serif; color: var(--white); }

  .hero { position: absolute; left: 0; top: 0; width: 1200px; height: 824px; background: var(--hero-bg); overflow: hidden; }
  .hero-photo {
    position: absolute; left: 0; top: 0; width: 940px; height: 824px;
    background: linear-gradient(180deg, var(--photo-dark) 0%, #6e5141 50%, var(--photo-warm) 100%);
  }

  .contact-panel { position: absolute; left: 0; top: 206px; width: 598px; height: 341px; background: var(--panel); }
  .contact-title {
    position: absolute; left: 212px; top: 189px;
    font-size: 37px; font-weight: 700; color: var(--tiffany); letter-spacing: 0.3px; line-height: 1;
  }
  .contact-details { position: absolute; left: 261px; top: 252px; width: 296px; font-size: 14px; font-style: italic; line-height: 14.5px; }
  .contact-details .address { position: absolute; left: 0; top: 0; }
  .contact-details .reach { position: absolute; right: 0; top: 0; text-align: right; }
  .contact-intro { position: absolute; left: 261px; top: 313px; font-size: 14px; line-height: 14.5px; }

  .contact-form { position: absolute; left: 261px; top: 369px; width: 296px; font-size: 14px; }
  .form-row { position: absolute; left: 0; width: 296px; }
  .form-row label { position: absolute; left: 0; top: -1px; }
  .form-row .field { position: absolute; left: 82px; top: 0; width: 214px; background: var(--field); border: 0; resize: none; }
  .row-name { top: 0; } .row-name .field { height: 18px; }
  .row-email { top: 28px; } .row-email .field { height: 18px; }
  .row-message { top: 58px; } .row-message .field { height: 72px; }
  .send-button {
    position: absolute; left: 254px; top: 141px; width: 42px; height: 18px;
    background: var(--white); color: var(--tiffany); font-family: inherit; font-style: italic; font-size: 13px; border: 0; line-height: 18px;
  }

  .brand-box {
    position: absolute; left: 624px; top: 206px; width: 326px; height: 130px;
    background: linear-gradient(90deg, var(--tiffany-deep) 0%, #2ba39d 45%, var(--tiffany-light) 100%);
  }
  .brand-name {
    position: absolute; left: 629px; top: 194px; font-size: 38px; font-weight: 700; line-height: 36px; color: var(--white); letter-spacing: -0.2px;
  }
  .main-nav { position: absolute; left: 636px; top: 318px; display: flex; gap: 18px; font-size: 13.5px; }
  .main-nav a { color: var(--white); text-decoration: none; }
  .main-nav a.is-active { color: var(--nav-active); font-weight: 700; }

  .site-footer { position: absolute; left: 0; top: 857px; width: 595px; height: 132px; background: var(--footer-bg); }
  .footer-col { position: absolute; top: 871px; font-size: 14px; line-height: 14.5px; }
  .footer-col h2 { font-size: 14px; font-weight: 400; color: var(--tiffany); margin-bottom: 11px; }
  .footer-col p { font-style: italic; color: var(--ink-muted); margin-bottom: 14.5px; }
  .footer-services { left: 261px; }
  .footer-find { left: 421px; }
</style>
</head>
<body>
  <section class="hero">
    <div class="hero-photo" role="img" aria-label="Portrait photograph of a woman with voluminous curly hair"></div>
    <div class="contact-panel"></div>
  </section>

  <h1 class="contact-title">CONTACT US</h1>

  <div class="contact-details">
    <p class="address">Level 2,<br>18 Fern Lane, Millbrook,<br>Harbourton, Australia.</p>
    <p class="reach">1800 45 61 07<br>hello@curlbar.com</p>
  </div>

  <p class="contact-intro">If you have any questions or comments,<br>please leave a message.</p>

  <form class="contact-form">
    <div class="form-row row-name"><label for="name">Name</label><input class="field" id="name" type="text"></div>
    <div class="form-row row-email"><label for="email">Email</label><input class="field" id="email" type="email"></div>
    <div class="form-row row-message"><label for="message">Message</label><textarea class="field" id="message"></textarea></div>
    <button class="send-button" type="button">send</button>
  </form>

  <div class="brand-box"></div>
  <p class="brand-name">BLOW DRY AND<br>HAIR EXTENSION<br>BOUTIQUE</p>
  <nav class="main-nav">
    <a href="#">About us</a>
    <a href="#">Bow Dry</a>
    <a href="#">Hair Extention</a>
    <a href="#" class="is-active">Contact us</a>
  </nav>

  <footer class="site-footer"></footer>
  <div class="footer-col footer-services">
    <h2>Services</h2>
    <p>Bow Dry<br>Hair Extensions</p>
    <p>About Us<br>Contact Us</p>
  </div>
  <div class="footer-col footer-find">
    <h2>Where to find us</h2>
    <p>1800 45 61 07</p>
    <p>Level 2,<br>18 Fern Lane, Millbrook,<br>Harbourton, Australia.</p>
  </div>
</body>
</html>
```